Marwick Agency (http://mk.fennoweb-studio.com/)

We are looking for a similar design to what we have, but more professional looking and cleaned up with links and logo that is not so grainy looking. We are an independent insurance agency marketing to personal and commercial clients. We offer all commercial lines markets and all personal lines. We target excavators, landscapers, restaurants, golf courses, contractors. Please look at http://mk.fennoweb-studio.com/ which we had designed but do not like it, it will give you an idea of what we are looking for.

Target Market(s)

Commercial and personal insurance. All business products and all personal (homeowners, auto, antique auto, umbrella)

Industry/Entity Type

It Professional

Logo Text

Knowledge Building Your Assurance

Number of Pages Required

5+ page

Colors
000000
848484
0255a3

```html
<!DOCTYPE html>
<html lang="en">
<head>
<meta charset="utf-8">
<title>Marwick Agency – Contact Us</title>
<link href="https://fonts.googleapis.com/css2?family=Open+Sans:wght@300;400;600;700&display=swap" rel="stylesheet">
<style>
:root{
  --blue:#1676c9;
  --blue-dark:#0f5fa6;
  --ink:#2b2b2b;
  --text:#555;
  --muted:#8a8a8a;
  --line:#dcdcdc;
  --field:#d6d6d6;
  --band:#f2f2f2;
  --footer:#36393d;
  --footer-bottom:#2b2d30;
  --footer-text:#c9c9c9;
  --white:#fff;
}
*{box-sizing:border-box;margin:0;padding:0}
html,body{width:976px;height:1200px;overflow:hidden}
body{position:relative;background:var(--white);font-family:'Open Sans',Arial,sans-serif;color:var(--text)}
.abs{position:absolute}

/* top bar */
.topbar{left:0;top:0;width:976px;height:29px;border-bottom:1px solid #ececec}
.topbar .contact{left:71px;top:9px;font-size:8.5px;color:var(--muted)}
.topbar .contact b{font-weight:600;color:#666}
.topbar .social{left:782px;top:9px;display:flex;gap:14px}
.social-dot{width:12px;height:12px;border-radius:50%;background:#c4c4c4}
.social-dot.active{background:var(--blue)}
.topbar .social-line{left:782px;top:27px;width:76px;height:2px;background:var(--blue)}

/* header */
.header{left:0;top:29px;width:976px;height:64px;background:var(--white)}
.brand{left:71px;top:19px;font-size:21px;color:var(--ink);font-weight:400}
.nav{right:69px;top:25px;display:flex;gap:0;font-size:11.5px;color:#333}
.nav a{color:#333;text-decoration:none;margin-left:22px}
.nav a.current{color:var(--blue)}
.hero-shade{left:0;top:93px;width:976px;height:110px;background:linear-gradient(#ececec,#fff)}
.hero-shadow{left:90px;top:93px;width:796px;height:10px;border-radius:50%;box-shadow:0 6px 10px rgba(0,0,0,.18)}

/* page title */
.page-title{left:71px;top:135px;font-size:18px;color:var(--blue);font-weight:400}
.crumbs{left:192px;top:143px;font-size:8.5px;color:var(--muted)}
.crumbs span{text-decoration:underline}
.title-rule{left:71px;top:174px;width:836px;height:1px;background:var(--line)}
.title-accent{left:71px;top:173px;width:63px;height:3px;background:var(--blue)}
.search{left:687px;top:135px;width:220px;height:26px;border:1px solid var(--line);background:var(--white)}
.search span{position:absolute;left:8px;top:7px;font-size:8.5px;color:#aaa}
.search .go{position:absolute;right:-1px;top:-1px;width:27px;height:26px;background:var(--blue)}

/* section headings */
.h2{top:192px;font-size:27px;font-weight:300;color:#333}

/* form */
.form-head{left:71px;top:247px;width:402px;height:32px;background:var(--blue);color:var(--white);font-size:11px}
.form-head .icon{position:absolute;left:0;top:0;width:32px;height:32px;border-right:1px solid rgba(255,255,255,.35)}
.form-head .label{position:absolute;left:42px;top:9px}
.field{border:1px solid var(--field);box-shadow:inset 0 0 0 2px #f4f4f4;background:var(--white);font-size:8.5px;color:#888;font-weight:600}
.field span{position:absolute;left:9px;top:10px}
.field i{color:var(--blue);font-style:normal}
.send{left:384px;top:569px;width:89px;height:30px;background:var(--blue);color:var(--white);font-size:10.5px;text-align:center;line-height:30px}

/* address */
.map{left:501px;top:245px;width:406px;height:152px;background:linear-gradient(135deg,#e8e2cf 0%,#d9d6c0 45%,#bcd3e6 62%,#e6e0cd 80%,#dcd6bf 100%)}
.office{top:411px;font-size:11px;line-height:16px;color:#444}
.contact-row{height:24px;font-size:9.5px;color:var(--muted)}
.contact-row .ic{position:absolute;left:0;top:0;width:24px;height:24px;background:#b9b9b9}
.contact-row .txt{position:absolute;left:32px;top:6px}
.contact-row b{color:#333;font-weight:600}
.row-rule{height:1px;background:var(--line)}

/* banner */
.banner{left:71px;top:648px;width:836px;height:132px;background:var(--band);border-bottom:3px solid var(--blue)}
.banner h3{position:absolute;left:60px;top:31px;font-size:24px;font-weight:300;color:var(--blue);letter-spacing:.2px}
.banner p{position:absolute;left:103px;top:73px;font-size:9.5px;color:#444}
.hours{left:729px;top:663px;width:142px;height:104px;background:var(--blue-dark);color:var(--white);box-shadow:0 2px 3px rgba(0,0,0,.2)}
.hours .t{position:absolute;left:14px;top:10px;font-size:11.5px}
.hours .rule{position:absolute;left:0;top:36px;width:142px;height:1px;background:rgba(255,255,255,.3)}
.hours .d{position:absolute;left:0;width:142px;top:57px;text-align:center;font-size:8.5px;font-weight:700}

/* footer */
.footer{left:0;top:831px;width:976px;height:313px;background:var(--footer);color:var(--footer-text)}
.f-col{top:60px;font-size:9px;line-height:13px}
.f-head{font-size:11px;font-weight:700;color:var(--white);margin-bottom:22px;letter-spacing:.3px}
.f-logo{font-size:21px;color:var(--white);margin-top:-5px;margin-bottom:14px}
.f-item{position:relative;padding-left:21px;margin-bottom:14px}
.f-item svg{position:absolute;left:0;top:1px}
.post{position:relative;padding-left:12px;margin-bottom:10px;color:#e6e6e6}
.post:before{content:"›";position:absolute;left:0;top:-2px;font-size:12px}
.post small{display:block;color:#5eaef0;font-size:7.5px}
.post b{color:#fff;font-weight:600}
.sub-field{display:flex;margin-top:-6px}
.sub-field span{width:128px;height:20px;background:var(--white);color:#aaa;font-size:8.5px;padding:4px 7px}
.sub-field em{width:63px;height:20px;background:var(--blue);color:#fff;font-style:normal;font-size:9px;text-align:center;line-height:20px}
.f-social{display:flex;gap:20px;margin-top:-8px}
.f-social div{width:16px;height:16px;border-radius:50%;background:#6b6e72}
.f-social div.active{background:var(--blue)}
.footer-bottom{left:0;top:1144px;width:976px;height:56px;background:var(--footer-bottom);font-size:8.5px;color:#d5d5d5}
.footer-bottom .copy{position:absolute;left:71px;top:22px}
.footer-bottom nav{position:absolute;right:70px;top:22px;display:flex;gap:23px}
</style>
</head>
<body>

<div class="abs topbar">
  <div class="abs contact"><b>Call Us Today!</b> &nbsp;1-888-4 MARWICK &nbsp;| &nbsp;admin@marwickagency.com</div>
  <div class="abs social" aria-label="Social links">
    <div class="social-dot active"></div><div class="social-dot"></div><div class="social-dot"></div><div class="social-dot"></div><div class="social-dot"></div>
  </div>
  <div class="abs social-line"></div>
</div>

<div class="abs hero-shade"></div>
<div class="abs hero-shadow"></div>
<header class="abs header">
  <div class="abs brand">Marwick Agency</div>
  <nav class="abs nav">
    <a>Home</a><a>Personal Insurance</a><a>Business Insurance</a><a>About Us</a><a class="current">Contact Us</a><a>More</a>
  </nav>
</header>

<div class="abs page-title">Contact Us</div>
<div class="abs crumbs"><span>Home</span> &nbsp;›&nbsp; <span>Contact US</span></div>
<div class="abs title-rule"></div>
<div class="abs title-accent"></div>
<div class="abs search"><span>To search enter keyword</span>
  <div class="go"><svg width="27" height="26" viewBox="0 0 27 26"><path d="M10 9l4 4-4 4M14 9l4 4-4 4" stroke="#fff" stroke-width="1.5" fill="none"/></svg></div>
</div>

<h2 class="abs h2" style="left:70px">Online Appointment Form</h2>
<h2 class="abs h2" style="left:498px">Address &amp; Contact</h2>

<div class="abs form-head">
  <div class="icon"><svg width="32" height="32" viewBox="0 0 32 32"><circle cx="16" cy="12.5" r="3.5" fill="#fff"/><path d="M10 22c0-4 3-6 6-6s6 2 6 6z" fill="#fff"/></svg></div>
  <div class="label">Marwick Agency</div>
  <svg class="abs" style="right:10px;top:9px" width="14" height="14" viewBox="0 0 14 14"><path d="M7 0v14M0 7h14" stroke="#fff" stroke-width="1"/></svg>
</div>
<div class="abs field" style="left:71px;top:295px;width:194px;height:29px"><span>First Name <i>*</i></span></div>
<div class="abs field" style="left:279px;top:295px;width:194px;height:29px"><span>Last Name <i>*</i></span></div>
<div class="abs field" style="left:71px;top:339px;width:194px;height:29px"><span>Phone Number <i>*</i></span></div>
<div class="abs field" style="left:279px;top:339px;width:194px;height:29px"><span>E-mail <i>*</i></span></div>
<div class="abs field" style="left:71px;top:399px;width:402px;height:157px"><span>Reason of Appointment</span></div>
<div class="abs send">Send &nbsp;›</div>

<div class="abs map" role="img" aria-label="Street map of the New Jersey and New York area showing office locations"></div>

<div class="abs office" style="left:501px">Fairhollow Office:<br>Marwick Agency 214 Elm Street,<br>Suite C Fairhollow, NJ 08801</div>
<div class="abs office" style="left:717px">Brookhaven Office:<br>Marwick Agency<br>PO Box 742<br>56 South Pine Street<br>Brookhaven, NJ 08092</div>

<div class="abs contact-row" style="left:501px;top:495px;width:186px"><div class="ic"><svg width="24" height="24" viewBox="0 0 24 24"><path d="M8 7c1 0 2 2 2 3l-1 1c1 2 2 3 4 4l1-1c1 0 3 1 3 2l-1 2c-5 0-9-4-10-9z" fill="#fff"/></svg></div><div class="txt">Phone: <b>908-555-0120</b></div></div>
<div class="abs row-rule" style="left:501px;top:526px;width:186px"></div>
<div class="abs contact-row" style="left:501px;top:534px;width:186px"><div class="ic"><svg width="24" height="24" viewBox="0 0 24 24"><rect x="8" y="6" width="8" height="4" fill="#fff"/><rect x="6" y="10" width="12" height="6" fill="#fff"/><rect x="8" y="14" width="8" height="4" fill="#fff" stroke="#b9b9b9"/></svg></div><div class="txt">Fax: <b>908-555-0173</b></div></div>

<div class="abs contact-row" style="left:717px;top:495px;width:190px"><div class="ic"><svg width="24" height="24" viewBox="0 0 24 24"><path d="M8 7c1 0 2 2 2 3l-1 1c1 2 2 3 4 4l1-1c1 0 3 1 3 2l-1 2c-5 0-9-4-10-9z" fill="#fff"/></svg></div><div class="txt">Phone: <b>(609) 555-0188</b></div></div>
<div class="abs row-rule" style="left:717px;top:526px;width:190px"></div>
<div class="abs contact-row" style="left:717px;top:534px;width:190px"><div class="ic"><svg width="24" height="24" viewBox="0 0 24 24"><rect x="8" y="6" width="8" height="4" fill="#fff"/><rect x="6" y="10" width="12" height="6" fill="#fff"/><rect x="8" y="14" width="8" height="4" fill="#fff" stroke="#b9b9b9"/></svg></div><div class="txt">Fax: <b>(609) 555-0188</b></div></div>

<section class="abs banner">
  <h3>WE WANT TO KNOW AND WE WANT TO HELP</h3>
  <p>Whether you have a question or just want to discuss your options , our agents are always willing to help.</p>
</section>
<div class="abs hours">
  <div class="t">We Are Open From</div>
  <div class="rule"></div>
  <div class="d">Monday - Friday &nbsp;7:00 &nbsp;- 17.00</div>
  <svg class="abs" style="right:0;bottom:0" width="14" height="14" viewBox="0 0 14 14"><path d="M14 0L0 14h14z" fill="#fff"/><path d="M14 0L0 14h14" fill="none"/><path d="M14 0L0 14L14 0z" fill="#0b4a83"/><path d="M14 0L0 14L0 0z" fill="#0b4a83" opacity="0"/></svg>
</div>

<footer class="abs footer">
  <div class="abs f-col" style="left:70px;width:190px">
    <div class="f-logo">Marwick Agency</div>
    <div style="margin-bottom:22px">Your Slofan Or short Description<br>Goes Here</div>
    <div class="f-item"><svg width="10" height="12" viewBox="0 0 10 12"><path d="M5 0a4 4 0 014 4c0 3-4 8-4 8S1 7 1 4a4 4 0 014-4z" fill="#ccc"/><circle cx="5" cy="4" r="1.5" fill="#36393d"/></svg>Marwick Agency<br>PO Box 742<br>56 South Pine Street<br>Brookhaven, NJ 08092</div>
    <div class="f-item" style="margin-top:-14px;margin-bottom:0"><svg width="10" height="10" viewBox="0 0 10 10"><path d="M2 0c1 0 2 2 2 3L3 4c1 1 2 2 3 3l1-1c1 0 3 1 3 2L9 10C4 10 0 6 0 1z" fill="#ccc"/></svg>Phone: (609) 555-0188</div>
    <div class="f-item"><svg width="11" height="10" viewBox="0 0 11 10"><rect x="2" y="0" width="7" height="3" fill="#ccc"/><rect x="0" y="3" width="11" height="5" fill="#ccc"/><rect x="2" y="6" width="7" height="4" fill="#ccc" stroke="#36393d"/></svg>Fax: (609) 555-0170</div>
    <div class="f-item" style="margin-top:4px"><svg width="11" height="8" viewBox="0 0 11 8"><rect width="11" height="8" fill="#ccc"/><path d="M0 0l5.5 4L11 0" stroke="#36393d" fill="none"/></svg>admin@marwickagency.com</div>
  </div>

  <div class="abs f-col" style="left:279px;width:190px">
    <div class="f-head">RECENT POSTS</div>
    <div class="post">Consecte tur adipiscing elit ut eunt<small>3 days ago</small></div>
    <div class="post">Fusce vel tempus augue nunc<small>5 days ago</small></div>
    <div class="post">Lorem nulla, vitae eleifend leo tincidunt<small>7 days ago</small></div>
  </div>

  <div class="abs f-col" style="left:488px;width:190px">
    <div class="f-head">RECENT TWEETS</div>
    <div class="post">Integer iaculis egestas odio, vel dictum turpis placerat id. Pellentesque semper nisl eget: <b>t.co/Xq7mLp2Rv</b><small style="margin-top:6px">2 days ago</small></div>
    <div class="post" style="margin-top:16px">Curabitur consequat tortor ut eros posu ere rutrum donec metus nisl, dictum vita fermentum: <b>t.co/Xq7mLp2Rv</b><small style="margin-top:6px">6 days ago</small></div>
  </div>

  <div class="abs f-col" style="left:697px;width:210px">
    <div class="f-head">NEWSLETTER</div>
    <div style="margin-bottom:22px">Get The latest News!</div>
    <div class="sub-field"><span>Email Address</span><em>Subscribe</em></div>
    <div class="f-head" style="margin-top:30px">SOCIAL MEDIA</div>
    <div class="f-social" aria-label="Social links"><div class="active"></div><div></div><div></div><div></div><div></div></div>
  </div>
</footer>

<div class="abs footer-bottom">
  <div class="copy">Copyright 2015 Marwick Agency | All Rights Reserved</div>
  <nav><span>Home</span><span>Personal Insurance</span><span>Business Insurance</span><span>Service Center</span><span>About Us</span><span>Contact Us</span></nav>
</div>

</body>
</html>
```